Research campaign for the global health issues in Africa must be modern, impactful and unique *

Please see attachment
Research campaign for the global health issues in Africa must be modern, impactful and unique
Updates

Please find the updated flyer requirement. These designs are not modern. We would need this flyer displayed on KD , Pelmora and vexalo. Please use either option of the requirement. Color scheme is Blue.

Target Market(s)

Patients, volunteers, patient advocacy groups, hospitals, healthcare professionals

Industry/Entity Type

Health Care

Font styles to use
Serif

Colors
0355a3
fbed22
f04a50

Requirements
Must have
• Please note that this must be a modern flyer that can be posted on Kandewick so size matters here.
Nice to have
• To see African/black people or foot print or shadow of a walk
• There can be a background image of a child’s face or Person walking or We could have a hand print or foot print with different disease colors.

```html
<!DOCTYPE html>
<html lang="en">
<head>
<meta charset="utf-8">
<title>Stride for World Health Research Movement 2019</title>
<link rel="stylesheet" href="https://fonts.googleapis.com/css2?family=Bebas+Neue&family=Oswald:wght@400;500;600&display=swap">
<style>
:root{
  --blue:#0355a3;
  --blue-dark:#0d4a8e;
  --red:#f04a50;
  --ink:#1b1b1b;
  --white:#ffffff;
  --sky-top:#9ccbe6;
  --sky-mid:#d8e9f2;
  --rule:#6f9cc6;
}
*{margin:0;padding:0;box-sizing:border-box}
html,body{width:1200px;height:1200px;overflow:hidden;background:#fff}
.flyer{position:relative;width:1200px;height:1200px;overflow:hidden;font-family:"Oswald",sans-serif;
  background:linear-gradient(180deg,var(--sky-top) 0%,var(--sky-mid) 40%,#e9e4da 70%,#d9d2c8 100%)}
.photo{position:absolute;left:312px;top:312px;width:723px;height:888px;
  background:linear-gradient(180deg,#7fb8db 0%,#b9d6e6 28%,#d48a2a 42%,#9c6a26 55%,#4e5a22 68%,#a27a52 80%,#c49a7c 100%)}
.photo-side{position:absolute;left:1035px;top:312px;width:165px;height:888px;background:rgba(255,255,255,.82)}
.sky-corner{position:absolute;left:0;top:0;width:300px;height:300px;
  background:linear-gradient(160deg,#5fa8d4 0%,#a9d0e8 45%,#e4f0f7 100%)}
.bar-v{position:absolute;left:300px;top:0;width:12px;height:1200px;background:var(--blue)}
.bar-h{position:absolute;left:0;top:300px;width:1200px;height:12px;background:var(--blue)}
.header{position:absolute;left:312px;top:0;width:888px;height:300px;background:rgba(255,255,255,.9);
  border-right:12px solid var(--blue);padding:28px 0 0 80px}
.title{font-family:"Bebas Neue",sans-serif;font-weight:400;color:var(--red);font-size:82px;line-height:88px;letter-spacing:1.5px}
.title-rule{width:718px;height:2px;background:var(--rule);margin:18px 0 12px}
.subtitle{font-family:"Bebas Neue",sans-serif;color:var(--blue);font-size:40px;letter-spacing:.3px}
.presenter{position:absolute;left:0;top:136px;width:300px;text-align:center;font-family:"Bebas Neue",sans-serif;font-size:27px;color:var(--ink)}
.tag-box{position:absolute;left:312px;top:312px;width:288px;height:288px;background:#fff;
  border-right:12px solid var(--blue);border-bottom:12px solid var(--blue);text-align:center;padding-top:84px}
.tag-slogan{font-family:"Bebas Neue",sans-serif;color:var(--blue);font-size:33px}
.tag-hash{font-family:"Bebas Neue",sans-serif;color:var(--blue);font-size:52px;margin-top:14px}
.route{position:absolute;left:0;top:312px;width:300px;height:888px;background:rgba(255,255,255,.55);text-align:center}
.route-head{font-family:"Bebas Neue",sans-serif;font-size:50px;color:var(--ink);margin-top:42px}
.route-word{font-family:"Bebas Neue",sans-serif;font-size:36px;color:var(--ink)}
.route-place{font-family:"Bebas Neue",sans-serif;font-size:36px;color:var(--blue);line-height:36px}
.route-rule{width:196px;height:2px;background:var(--rule);margin:0 auto}
.date{font-family:"Bebas Neue",sans-serif;font-size:38px;line-height:48px;color:var(--ink)}
.csr{font-family:"Bebas Neue",sans-serif;font-size:24px;color:var(--ink)}
.enq{font-family:"Bebas Neue",sans-serif;font-size:24px;color:var(--blue)}
.phone{font-family:"Bebas Neue",sans-serif;font-size:38px;color:var(--blue)}
.perk{position:absolute;left:312px;width:288px;background:rgba(255,255,255,.45);text-align:center;
  font-family:"Bebas Neue",sans-serif;color:#fff;font-size:30px;line-height:36px;
  text-shadow:0 0 2px var(--blue-dark),1px 1px 0 var(--blue-dark),-1px -1px 0 var(--blue-dark)}
.partners{position:absolute;left:1045px;top:330px;width:148px;list-style:none}
.partner{display:flex;align-items:center;gap:6px;height:72px;font-family:"Oswald",sans-serif;font-weight:500;font-size:14px;color:var(--blue);line-height:16px}
.partner-dot{flex:0 0 22px;height:22px;border-radius:50%;background:var(--blue)}
</style>
</head>
<body>
<main class="flyer">
  <div class="sky-corner"></div>
  <div class="photo" role="img" aria-label="Photo of a young girl carrying a water container on her head, walking away down a sunlit road lined with trees"></div>
  <div class="photo-side"></div>

  <p class="presenter">NORVALE RESEARCH PRESENTS</p>

  <header class="header">
    <h1 class="title">STRIDE FOR WORLD HEALTH<br>RESEARCH MOVEMENT 2019</h1>
    <div class="title-rule"></div>
    <p class="subtitle">IN COMMEMORATION OF THE WORLD CLINICAL TRIALS DAY</p>
  </header>

  <div class="bar-v"></div>
  <div class="bar-h"></div>

  <section class="route">
    <h2 class="route-head">WALK ROUTE:</h2>
    <p class="route-word" style="margin-top:28px">FROM</p>
    <p class="route-place" style="margin-top:14px">HARLOW (EDE-LANU)<br>GATE</p>
    <p class="route-word" style="margin-top:22px">TO</p>
    <p class="route-place" style="margin-top:16px;line-height:46px">CIVIC<br>STADIUM ORWENU</p>
    <div class="route-rule" style="margin-top:28px"></div>
    <p class="date" style="margin-top:38px">SATURDAY, MAY 25<br>2019<br>AT 6:00 AM</p>
    <div class="route-rule" style="margin-top:34px"></div>
    <p class="csr" style="margin-top:36px">NORVALE RESEARCH CSR INITIATIVE</p>
    <p class="enq" style="margin-top:6px">FOR ENQUIRES PLEASE CONTACT:</p>
    <p class="phone">+2348015550172</p>
  </section>

  <div class="tag-box">
    <p class="tag-slogan">HEALINGBEGINSWITHUS</p>
    <p class="tag-hash">#SFWHRM19</p>
  </div>

  <p class="perk" style="top:652px;height:84px;padding-top:6px">FREE HEALTH SCREENING<br>AND CONSULTATION</p>
  <p class="perk" style="top:778px;height:44px;padding-top:4px">ENTERTAINMENT</p>
  <p class="perk" style="top:864px;height:44px;padding-top:4px">REFRESHMENT</p>
  <p class="perk" style="top:950px;height:44px;padding-top:4px">RAFFLE PRIZE</p>
  <p class="perk" style="top:1038px;height:44px;padding-top:4px">COMPLIMENTARY T-SHIRTS</p>
  <p class="perk" style="top:1125px;height:44px;padding-top:4px">INFORMATIVE SESSIONS</p>

  <ul class="partners">
    <li class="partner"><span class="partner-dot"></span>Medvera Agency</li>
    <li class="partner"><span class="partner-dot"></span>Lumaro Initiative</li>
    <li class="partner">Trialcare Assoc.</li>
    <li class="partner">The Healthlink Web</li>
    <li class="partner"><span class="partner-dot"></span>Neura Women</li>
    <li class="partner">Tessaly Fund</li>
    <li class="partner"><span class="partner-dot"></span>Vaxora Society</li>
    <li class="partner"><span class="partner-dot"></span>Doreth Care Fund</li>
    <li class="partner">Ovell Foundation</li>
    <li class="partner">Redloop SCI</li>
    <li class="partner">Shoreline Clinics</li>
    <li class="partner">Vitawell</li>
  </ul>
</main>
</body>
</html>
```